LineUp Banner for EDM music Festival!

Hello,

i need a lineup banner for an edm festival.

It should looks similar to the lineup banner uploaded here. I also added the background image.

Feel free to add something you think it looks cool.
Background have to be used. I would need after your work is done the psd file, so I can edit the text / names by myself.

Size should be around 2000x3000.

Thank you

Industry/Entity Type

Festival

Requirements
Must have
• Similar to the lineup banner. Feel free to add something you think it looks cool.
• Background have to be used.
Nice to have
• In best case it will be as most similar as the uploaded lineup banner.

```html
<!DOCTYPE html>
<html lang="en">
<head>
<meta charset="utf-8">
<title>AAA Festival – Lineup</title>
<link rel="stylesheet" href="https://fonts.googleapis.com/css2?family=Archivo+Black&family=Oswald:wght@500;700&family=Roboto+Condensed:wght@400;700&display=swap">
<style>
  :root {
    --ink: #050505;
    --white: #ffffff;
    --gold-light: #fff6b0;
    --gold: #ffcc1a;
    --orange: #f08a12;
    --red: #d8261a;
    --cream: #f4e2b0;
    --magenta: #e34cc8;
  }
  html, body {
    margin: 0;
    padding: 0;
    overflow: hidden;
    background: var(--ink);
  }
  .poster {
    position: relative;
    width: 800px;
    height: 1200px;
    overflow: hidden;
    background: var(--ink);
    font-family: "Roboto Condensed", Arial, sans-serif;
    color: var(--white);
  }
  .backdrop {
    position: absolute;
    inset: 0;
    background:
      radial-gradient(ellipse 130px 90px at 120px 40px, rgba(227,76,200,.55), transparent 70%),
      radial-gradient(ellipse 320px 70px at 400px 195px, rgba(255,190,60,.75), transparent 75%),
      radial-gradient(ellipse 260px 120px at 400px 150px, rgba(240,110,20,.35), transparent 80%),
      radial-gradient(ellipse 520px 170px at 400px 560px, rgba(240,60,30,.9), transparent 75%),
      radial-gradient(ellipse 420px 200px at 380px 660px, rgba(244,226,176,.95), transparent 80%),
      radial-gradient(ellipse 600px 300px at 400px 760px, rgba(190,40,20,.8), transparent 80%),
      linear-gradient(180deg, #070707 0%, #0a0606 38%, #3a0d08 45%, #c83a1c 52%, #e9c98e 58%, #b4542a 66%, #4a1a10 76%, #120707 84%, #050505 90%, #050505 100%);
  }
  .presenter {
    position: absolute;
    top: 14px;
    left: 0;
    width: 800px;
    text-align: center;
    font-family: "Oswald", Arial, sans-serif;
    font-weight: 500;
    font-size: 46px;
    line-height: 1;
    letter-spacing: 1px;
  }
  .festival-title {
    position: absolute;
    top: 84px;
    left: 0;
    width: 800px;
    text-align: center;
    margin: 0;
    font-family: "Oswald", Arial, sans-serif;
    font-weight: 700;
    font-size: 132px;
    line-height: 1;
    letter-spacing: 1px;
    background: linear-gradient(90deg, var(--white) 18%, var(--gold-light) 35%, var(--gold) 55%, var(--orange) 80%);
    -webkit-background-clip: text;
    background-clip: text;
    color: transparent;
  }
  .event-date {
    position: absolute;
    top: 296px;
    left: 0;
    width: 800px;
    text-align: center;
    font-family: "Archivo Black", Arial, sans-serif;
    font-size: 54px;
    line-height: 1;
    background: linear-gradient(180deg, var(--gold-light) 0%, var(--gold) 45%, var(--orange) 100%);
    -webkit-background-clip: text;
    background-clip: text;
    color: transparent;
  }
  .lineup {
    position: absolute;
    top: 410px;
    left: 45px;
    width: 712px;
    margin: 0;
    padding: 0;
    list-style: none;
    display: grid;
    grid-template-columns: 377px 335px;
    row-gap: 6px;
    font-family: "Roboto Condensed", Arial, sans-serif;
    font-weight: 700;
    font-size: 46px;
    line-height: 52px;
    white-space: nowrap;
  }
  .info {
    position: absolute;
    top: 970px;
    left: 0;
    width: 800px;
    font-size: 19px;
  }
  .info-heading {
    text-align: center;
    margin: 0 0 20px;
    font-weight: 400;
    font-size: 20px;
  }
  .info-grid {
    margin: 0;
    padding: 0;
    list-style: none;
    display: grid;
    grid-template-columns: 251px 261px 210px;
    margin-left: 40px;
    row-gap: 8px;
    white-space: nowrap;
  }
  .info-grid li { line-height: 22px; }
  .sponsors {
    position: absolute;
    top: 1124px;
    left: 0;
    width: 800px;
    display: flex;
    align-items: center;
    gap: 14px;
  }
  .sponsors-rule {
    flex: 1;
    height: 2px;
    background: var(--white);
  }
  .sponsors-label {
    font-weight: 700;
    font-size: 20px;
  }
  .sponsor-slots {
    position: absolute;
    top: 1155px;
    left: 225px;
    display: flex;
    gap: 4px;
  }
  .sponsor-slot {
    width: 31px;
    height: 33px;
    background: var(--white);
  }
</style>
</head>
<body>
<main class="poster">
  <div class="backdrop" role="img" aria-label="Festival crowd with raised hands in front of a glowing stage, under fireworks and colourful stage lights"></div>

  <div class="presenter">AAA PRESENT</div>
  <h1 class="festival-title">AAA FESTIVAL</h1>
  <div class="event-date">OCTOBER 31, SUNDAY</div>

  <ul class="lineup">
    <li>DJ ARTIST NAME</li>
    <li>DJ ARTIST NAME</li>
    <li>DJ ARTIST NAME</li>
    <li>DJ ARTIST NAME</li>
  </ul>

  <section class="info">
    <h2 class="info-heading">GENERAL INFORMATIONS</h2>
    <ul class="info-grid">
      <li>GENERAL INFORMATIONS ▪</li>
      <li>GENERAL INFORMATIONS ▪</li>
      <li>GENERAL INFORMATIONS</li>
      <li>GENERAL INFORMATIONS ▪</li>
      <li>GENERAL INFORMATIONS ▪</li>
      <li>GENERAL INFORMATIONS</li>
      <li>GENERAL INFORMATIONS ▪</li>
      <li>GENERAL INFORMATIONS ▪</li>
      <li>GENERAL INFORMATIONS</li>
    </ul>
  </section>

  <div class="sponsors">
    <span class="sponsors-rule"></span>
    <span class="sponsors-label">SPONSORS</span>
    <span class="sponsors-rule"></span>
  </div>
  <div class="sponsor-slots">
    <span class="sponsor-slot"></span>
    <span class="sponsor-slot"></span>
    <span class="sponsor-slot"></span>
    <span class="sponsor-slot"></span>
    <span class="sponsor-slot"></span>
    <span class="sponsor-slot"></span>
    <span class="sponsor-slot"></span>
    <span class="sponsor-slot"></span>
    <span class="sponsor-slot"></span>
  </div>
</main>
</body>
</html>
```